Bref créative
Stationery
Health centre
Bright & Fun-filled
Meadowlark Wellness Studio
We need cards for different individuals - easily editable
12B Harlow Terrace
Edinburgh
EH4 7QN
info@meadowlarkwellstudio.co.uk
www.meadowlarkwellstudio.co.uk
appointments date and time & cancelation policy.
We require 24 hours cancellation for appointments otherwise a charge may be incurred.

```html
<!DOCTYPE html>
<html lang="en">
<head>
<meta charset="utf-8">
<title>Meadowlark Wellness Studio – Stationery</title>
<link rel="stylesheet" href="https://fonts.googleapis.com/css2?family=Cinzel:wght@500&display=swap">
<style>
  :root{
    --page:#ffffff;
    --paper:#ffffff;
    --edge:#d9d9d9;
    --shadow:rgba(0,0,0,.12);
    --brand-green:#5e9a3c;
    --leaf-green:#8cc152;
    --sky-blue:#3d8fc6;
    --rule:#b9d7a4;
  }
  *{margin:0;padding:0;box-sizing:border-box}
  html,body{width:1200px;height:794px;overflow:hidden;background:var(--page)}
  body{position:relative;font-family:"Cinzel",Georgia,serif;color:var(--brand-green)}

  .sheet{position:absolute;background:var(--paper);border:1px solid var(--edge);box-shadow:1px 2px 4px var(--shadow)}

  .brand{display:flex;flex-direction:column;align-items:center;text-align:center}
  .brand__dot{border-radius:50%;background:var(--leaf-green)}
  .brand__name{font-weight:500;color:var(--brand-green);line-height:1.1;letter-spacing:.04em;text-transform:uppercase}

  /* Letterhead */
  .letterhead{left:96px;top:24px;width:487px;height:725px}
  .letterhead .brand{position:absolute;top:40px;left:0;right:0}
  .letterhead .brand__dot{width:30px;height:30px;margin-bottom:10px}
  .letterhead .brand__name{font-size:19px}
  .letterhead__footer{position:absolute;left:40px;right:40px;bottom:22px;font-size:8px;line-height:1.6;letter-spacing:.05em;color:var(--leaf-green);text-transform:uppercase}
  .letterhead__footer p:last-child{display:flex;justify-content:space-between}

  /* Business card */
  .card{top:146px;width:222px;height:149px}
  .card--profile{left:648px}
  .card--appointment{left:890px}
  .card--profile .brand{margin-top:16px}
  .card--profile .brand__dot{width:13px;height:13px;margin-bottom:5px}
  .card--profile .brand__name{font-size:9px}
  .card__role{margin-top:6px;text-align:center;font-size:6px;letter-spacing:.08em;color:var(--sky-blue);text-transform:uppercase}
  .card__contact{position:absolute;left:18px;bottom:20px;font-size:5.5px;line-height:1.55;letter-spacing:.04em;color:var(--leaf-green);text-transform:uppercase}

  .appointment__name{position:absolute;left:18px;right:18px;top:22px;display:flex;align-items:flex-end;gap:6px;font-size:6px;color:var(--sky-blue);text-transform:uppercase;letter-spacing:.06em}
  .appointment__name span.line{flex:1;border-bottom:1px solid var(--rule);height:8px}
  .appointment__second{position:absolute;left:18px;right:18px;top:40px;border-bottom:1px solid var(--rule)}
  .appointment__slots{position:absolute;left:18px;right:18px;top:66px;display:grid;grid-template-columns:repeat(6,1fr);row-gap:14px;column-gap:4px}
  .slot{font-size:5.5px;letter-spacing:.05em;color:var(--sky-blue);text-transform:uppercase;border-bottom:1px solid var(--rule);padding-bottom:5px;text-align:center}
  .appointment__policy{position:absolute;left:18px;right:18px;bottom:14px;font-size:5px;line-height:1.5;color:var(--leaf-green);text-align:center;font-family:Georgia,serif}

  /* Envelope */
  .envelope{left:648px;top:403px;width:463px;height:276px}
  .envelope__return{position:absolute;left:0;right:0;top:18px;transform:rotate(180deg);display:flex;flex-direction:column-reverse;align-items:center}
  .envelope__return .brand__dot{width:14px;height:14px;margin-bottom:4px}
  .envelope__return .brand__name{font-size:9px}
  .envelope__address{font-size:5.5px;letter-spacing:.05em;color:var(--leaf-green);text-transform:uppercase;margin-top:5px}
</style>
</head>
<body>

<section class="sheet letterhead" aria-label="Letterhead">
  <div class="brand">
    <span class="brand__dot"></span>
    <span class="brand__name">Meadowlark Wellness Studio</span>
  </div>
  <footer class="letterhead__footer">
    <p>12B Harlow Terrace, Edinburgh, EH4 7QN. Phone: 0131 496 0720</p>
    <p><span>info@meadowlarkwellstudio.co.uk</span><span>www.meadowlarkwellstudio.co.uk</span></p>
  </footer>
</section>

<section class="sheet card card--profile" aria-label="Business card front">
  <div class="brand">
    <span class="brand__dot"></span>
    <span class="brand__name">Meadowlark Wellness Studio</span>
  </div>
  <p class="card__role">Practitioner Name</p>
  <div class="card__contact">
    <p>12B Harlow Terrace, Edinburgh, EH4 7QN. 0131 496 0720</p>
    <p>info@meadowlarkwellstudio.co.uk</p>
    <p>www.meadowlarkwellstudio.co.uk</p>
  </div>
</section>

<section class="sheet card card--appointment" aria-label="Appointment card">
  <div class="appointment__name"><span>Name</span><span class="line"></span></div>
  <div class="appointment__second"></div>
  <div class="appointment__slots">
    <span class="slot">Mon</span><span class="slot">Tue</span><span class="slot">Wed</span>
    <span class="slot">Thu</span><span class="slot">Fri</span><span class="slot">Sat</span>
    <span class="slot">Date</span><span class="slot">Time</span><span class="slot">Date</span>
    <span class="slot">Time</span><span class="slot">Date</span><span class="slot">Time</span>
  </div>
  <p class="appointment__policy">We require 24 hours cancellation for appointments otherwise a charge may be incurred.</p>
</section>

<section class="sheet envelope" aria-label="Envelope">
  <div class="envelope__return">
    <div class="brand">
      <span class="brand__dot"></span>
      <span class="brand__name">Meadowlark Wellness Studio</span>
    </div>
    <p class="envelope__address">12B Harlow Terrace, Edinburgh, EH4 7QN</p>
  </div>
</section>

</body>
</html>
```